Professional website for psychological services

Create a professional, easy to navigate website using soothing coastal images and incorporate company logo in design. Website is for a small private clinic that provides psychological services and must be appealing to professional men and women. A website I really like is www.velmorlodge.example I would love something like similar.

Target Market(s)

Professional men and women seeking psychological services

Industry/Entity Type

Mental Health

Number of Pages Required

5+ page

Requirements
Must have
• The website must incorporate the logo provided. The name of the company/website is Brindle Oak Wellness Aftercare. Colors must compliment the logo, must be coastal and soothing yet very professional. I would like a website like www.velmorlodge.example
• Pages will be:Home, Services, FAQ and Contact Us. The images included of the building and office are for the contact us page. Under the tab Servies: Individual Psychotherapy, Family Therapy, EMDR I will provide specific content for each.
Nice to have
• I want the website to be easy to navigate and the font easy to read. The writing on the logo is very light and I'm open to changing it slightly if it will be better aesthetically.
Should not have
• Please no pictures of any swimsuits, alcoholic beverages, etc. This is a professional psychological clinic.

```html
<!DOCTYPE html>
<html lang="en">
<head>
<meta charset="utf-8">
<title>Brindle Oak Wellness Aftercare</title>
<link href="https://fonts.googleapis.com/css2?family=Noto+Serif:wght@400;700&family=Open+Sans:wght@400;600;700&display=swap" rel="stylesheet">
<style>
:root{
  --teal:#1fb8d6;
  --teal-deep:#0f9fc0;
  --sky:#19c3f0;
  --strip:#d4dad6;
  --sand:#f6e3d3;
  --sand-light:#fbefe6;
  --ink:#2d3238;
  --muted:#6b7279;
  --white:#ffffff;
  --footer-bar:#eeeeee;
  --ph-portrait:#c7bdb6;
  --ph-sea:#9fd3e6;
  --ph-sky:#c5dbe8;
  --ph-warm:#cfc6bf;
  --ph-light:#e3e0dc;
}
*{margin:0;padding:0;box-sizing:border-box}
html,body{width:699px;height:1200px;overflow:hidden;background:var(--white)}
body{font-family:"Open Sans",sans-serif;color:var(--ink);position:relative}

/* header */
.site-header{position:absolute;left:0;top:0;width:699px;height:118px;background:var(--white)}
.brand{position:absolute;left:0;right:0;top:22px;display:flex;justify-content:center;align-items:center;gap:8px}
.brand-dot{width:16px;height:16px;border-radius:50%;background:var(--teal)}
.brand-name{font-family:"Noto Serif",serif;font-size:26px;color:var(--teal-deep);font-weight:400}
.main-nav{position:absolute;top:90px;left:0;right:0;display:flex;justify-content:center;gap:22px;font-size:8px;font-weight:600;letter-spacing:.5px}
.main-nav a{color:var(--ink);text-decoration:none;padding:3px 8px}
.main-nav a.active{border:1px solid var(--ink);border-radius:2px}

/* hero */
.hero{position:absolute;left:0;top:118px;width:699px;height:220px;background:var(--sky)}
.hero-title{position:absolute;left:160px;top:104px;font-family:"Noto Serif",serif;font-weight:700;font-size:13px;color:var(--white);letter-spacing:.5px}
.hero-note{position:absolute;left:105px;top:123px;width:250px;height:60px;background:rgba(255,255,255,.35);padding:7px 10px 0 55px;font-size:7.5px;line-height:1.4;color:var(--white)}
.hero-sign{position:absolute;left:275px;top:166px;font-family:"Noto Serif",serif;font-size:11px;color:var(--ink)}
.hero-portrait{position:absolute;left:372px;top:34px;width:164px;height:164px;border-radius:50%;border:4px solid var(--white);background:var(--ph-portrait)}

/* photo strip */
.strip-top{position:absolute;left:0;top:338px;width:699px;height:14px;background:var(--strip)}
.gallery{position:absolute;left:0;top:352px;width:699px;height:132px;display:flex;gap:4px;background:var(--white)}
.gallery div{flex:1;height:100%}
.g1{background:var(--ph-sea)}
.g2{background:var(--ph-portrait)}
.g3{background:var(--ph-sea)}
.g4{background:var(--ph-sky)}
.g5{background:var(--ph-warm)}
.g6{background:var(--ph-light)}
.strip-bottom{position:absolute;left:0;top:484px;width:699px;height:16px;background:var(--strip)}

/* about */
.about{position:absolute;left:0;top:500px;width:699px;height:328px;background:linear-gradient(180deg,#3fcbf1 0%,#8fdbee 55%,var(--sand) 100%)}
.about-intro{position:absolute;left:137px;top:52px;font-family:"Noto Serif",serif;font-size:12px;color:var(--white)}
.about-title{position:absolute;left:137px;top:68px;font-family:"Noto Serif",serif;font-weight:700;font-size:16px;color:var(--white)}
.about-name{position:absolute;left:137px;top:96px;font-family:"Noto Serif",serif;font-size:11px;color:var(--white)}
.about-name b{font-weight:700}
.about-name small{font-size:7px}
.about-text{position:absolute;left:137px;width:225px;font-size:6.5px;line-height:1.55;color:var(--white)}
.about-text.p1{top:120px}
.about-text.p2{top:162px}
.about-phone{position:absolute;left:137px;top:212px;font-family:"Noto Serif",serif;font-weight:700;font-size:11px;color:var(--ink)}
.about-cta{position:absolute;left:137px;top:238px;background:var(--ink);color:var(--white);font-size:6px;font-weight:700;letter-spacing:.4px;padding:6px 12px}
.about-portrait{position:absolute;left:370px;top:28px;width:178px;height:240px;background:var(--ph-portrait)}

/* contact */
.contact{position:absolute;left:0;top:828px;width:699px;height:232px;background:linear-gradient(180deg,var(--sand) 0%,var(--sand-light) 100%)}
.contact-title{position:absolute;left:0;right:0;top:20px;text-align:center;font-family:"Noto Serif",serif;font-weight:700;font-size:16px;color:var(--ink)}
.contact-sub{position:absolute;left:0;right:0;top:42px;text-align:center;font-family:"Noto Serif",serif;font-size:9px;color:var(--ink)}
.field{position:absolute;height:18px;background:var(--white);border:1px solid #e6dbd2;font-size:6px;color:var(--muted);padding:5px 6px}
.f-name{left:233px;top:70px;width:108px}
.f-email{left:357px;top:70px;width:108px}
.f-phone{left:233px;top:98px;width:108px}
.f-date{left:357px;top:98px;width:108px}
.f-message{left:233px;top:128px;width:232px;height:56px}
.send{position:absolute;left:332px;top:198px;width:36px;height:14px;background:var(--teal);color:var(--white);font-size:6px;text-align:center;line-height:14px}

/* footer */
.site-footer{position:absolute;left:0;top:1060px;width:699px;height:115px;background:var(--white)}
.footer-brand{position:absolute;left:0;right:0;top:22px;display:flex;justify-content:center;align-items:center;gap:6px}
.footer-brand .brand-dot{width:12px;height:12px}
.footer-brand .brand-name{font-size:18px}
.social{position:absolute;left:0;right:0;top:70px;display:flex;justify-content:center;gap:8px}
.social span{width:20px;height:20px;border-radius:50%;background:#c9cdd0}
.copyright{position:absolute;left:0;top:1175px;width:699px;height:25px;background:var(--footer-bar);text-align:center;font-size:6px;line-height:25px;color:var(--muted)}
</style>
</head>
<body>

<header class="site-header">
  <div class="brand"><span class="brand-dot"></span><span class="brand-name">Brindle Oak</span></div>
  <nav class="main-nav">
    <a class="active" href="#">HOME</a>
    <a href="#">SERVICES</a>
    <a href="#">FAQ</a>
    <a href="#">CONTACT US</a>
  </nav>
</header>

<section class="hero">
  <h1 class="hero-title">RECOVERY AFTERCARE</h1>
  <p class="hero-note">We offer calm, confidential support for adults rebuilding balance after treatment, with care plans shaped around your life.</p>
  <span class="hero-sign">Brindle Oak</span>
  <div class="hero-portrait" role="img" aria-label="Round portrait photo of the psychologist"></div>
</section>

<div class="strip-top"></div>
<div class="gallery">
  <div class="g1" role="img" aria-label="Photo of a sunny beach with a palm tree"></div>
  <div class="g2" role="img" aria-label="Portrait photo of the psychologist"></div>
  <div class="g3" role="img" aria-label="Photo of a rocky coastline"></div>
  <div class="g4" role="img" aria-label="Photo of two friends raising their arms"></div>
  <div class="g5" role="img" aria-label="Photo of a person with their head in their hands"></div>
  <div class="g6" role="img" aria-label="Photo of a counselling session"></div>
</div>
<div class="strip-bottom"></div>

<section class="about" role="img" aria-label="Background photo of a calm sea and sandy beach">
  <p class="about-intro">Hi! do you need</p>
  <h2 class="about-title">Psychological Support ?</h2>
  <p class="about-name">I'm Doctor <b>Brindle Oak</b>, <small>psychologist</small></p>
  <p class="about-text p1">For over fifteen years I have helped professionals manage stress, anxiety and life transitions. Sessions are private, unhurried and built on evidence-based methods that respect your time and your goals.</p>
  <p class="about-text p2">Whether you are returning from residential care or simply feel stuck, we will work together on practical steps toward steadier days and healthier relationships at home and at work.</p>
  <p class="about-phone">Just Dial : +1 555 014 2290</p>
  <span class="about-cta">BOOK AN APPOINTMENT</span>
  <div class="about-portrait" role="img" aria-label="Portrait photo of the psychologist"></div>
</section>

<section class="contact">
  <h2 class="contact-title">Contact Brindle Oak</h2>
  <p class="contact-sub">Make an Appointment</p>
  <div class="field f-name">Name</div>
  <div class="field f-email">Email</div>
  <div class="field f-phone">Phone Number</div>
  <div class="field f-date">dd/mm/yyyy</div>
  <div class="field f-message">Message</div>
  <div class="send">Send</div>
</section>

<footer class="site-footer">
  <div class="footer-brand"><span class="brand-dot"></span><span class="brand-name">Brindle Oak</span></div>
  <div class="social"><span></span><span></span><span></span><span></span><span></span></div>
</footer>
<div class="copyright">Copyright 2024 All rights reserved</div>

</body>
</html>
```